Namecard design for Forex trading & training company

We need a design for a financial forex trading company.
Namecard should give customer a professional yet premium feel, able to differentiate from others.
1) most financial companies employs white background, while its clean and professional, it is too mainstream.
2) I am thinking of brown as base colour, however it easily gives the perception of being an Interior Design company
3) Task is to find a design that is able to portray a clean professional feel, at the same time, appear premium and differentiated from others.
*I'll be employing 3D textured print for my company namecard just so as to give it a better finishing.
Please find attached for my logo.
Financial

```html
<!DOCTYPE html>
<html lang="en">
<head>
<meta charset="utf-8">
<title>Corvane Capital – Business Card</title>
<link rel="stylesheet" href="https://fonts.googleapis.com/css2?family=Cormorant+Garamond:wght@500;600&family=Open+Sans:wght@400;600&display=swap">
<style>
  :root{
    --page:#e9e6e1;
    --card-white:#f7f7f7;
    --card-black:#121314;
    --card-black-soft:#2a2c2e;
    --brand-violet:#6a3fc4;
    --brand-magenta:#a4327f;
    --brand-rose:#e2475f;
    --brand-blue:#5a6fd8;
    --text-light:#f1f1f1;
    --text-muted:#c9c9c9;
  }
  *{margin:0;padding:0;box-sizing:border-box}
  html,body{width:1200px;height:1023px;overflow:hidden;background:var(--page)}
  .stage{position:relative;width:1200px;height:1023px}
  .card{position:absolute;width:540px;height:310px;top:356px;border-radius:4px;overflow:hidden;box-shadow:0 10px 30px rgba(0,0,0,.25)}
  .card--front{left:45px;background:var(--card-white)}
  .card--back{left:615px;background:linear-gradient(135deg,var(--card-black-soft) 0%,var(--card-black) 55%)}
  .card__shapes{position:absolute;inset:0}
  .brand{position:absolute;display:flex;align-items:center;gap:10px;font-family:"Cormorant Garamond",serif;font-weight:600;letter-spacing:.28em;text-transform:uppercase;color:var(--brand-blue)}
  .brand__mark{width:14px;height:14px;background:var(--brand-blue)}
  .card--front .brand{left:40px;top:48px;font-size:20px}
  .card--back .brand{left:0;right:0;top:140px;justify-content:center;font-size:24px}
  .person{position:absolute;left:34px;top:188px;color:var(--text-light)}
  .person__name{font-family:"Cormorant Garamond",serif;font-weight:500;font-size:26px;letter-spacing:.06em;text-transform:uppercase;line-height:1}
  .person__role{font-family:"Open Sans",sans-serif;font-size:10.5px;letter-spacing:.06em;text-transform:uppercase;color:var(--text-muted);margin-top:4px}
  .contact{list-style:none;margin-top:10px;font-family:"Open Sans",sans-serif;font-size:11.5px;color:var(--text-light)}
  .contact li{display:flex;align-items:center;gap:8px;line-height:17px}
  .contact svg{width:11px;height:11px;flex:none}
  .address{position:absolute;right:30px;top:170px;text-align:right;font-family:"Open Sans",sans-serif;font-size:13px;line-height:19px;letter-spacing:.02em;text-transform:uppercase;color:var(--text-light)}
</style>
</head>
<body>
<main class="stage">

  <section class="card card--front" aria-label="Business card front">
    <svg class="card__shapes" viewBox="0 0 540 310" aria-hidden="true">
      <defs>
        <linearGradient id="accentBand" x1="1" y1="0" x2="0" y2="0">
          <stop offset="0" stop-color="var(--brand-violet)"/>
          <stop offset=".55" stop-color="var(--brand-magenta)"/>
          <stop offset="1" stop-color="var(--brand-rose)"/>
        </linearGradient>
        <linearGradient id="darkPanel" x1="0" y1="0" x2="1" y2="1">
          <stop offset="0" stop-color="#2b2d2f"/>
          <stop offset=".6" stop-color="#131415"/>
          <stop offset="1" stop-color="#0c0c0d"/>
        </linearGradient>
      </defs>
      <polygon points="0,162 210,162 232,140 540,140 540,310 0,310" fill="url(#darkPanel)"/>
      <polygon points="214,154 236,132 540,132 540,120 230,120 214,136" fill="url(#accentBand)"/>
    </svg>

    <div class="brand"><span class="brand__mark"></span>Corvane Capital</div>

    <div class="person">
      <h1 class="person__name">Dorian Hale</h1>
      <p class="person__role">Pantry Manager</p>
      <ul class="contact">
        <li><svg viewBox="0 0 12 12" aria-hidden="true"><rect width="12" height="12" rx="1.5" fill="var(--text-light)"/><path d="M3.2 2.6l1.3-.2.6 1.7-.8.6a5 5 0 0 0 2.1 2.1l.6-.8 1.7.6-.2 1.3C6.2 8.4 3.6 5.8 3.2 2.6z" fill="var(--card-black)"/></svg>0210 555 0142</li>
        <li><svg viewBox="0 0 12 12" aria-hidden="true"><rect width="12" height="12" rx="1.5" fill="var(--text-light)"/><circle cx="6" cy="6" r="3.4" fill="none" stroke="var(--card-black)" stroke-width="1"/><path d="M2.6 6h6.8M6 2.6c-1.6 2-1.6 4.8 0 6.8M6 2.6c1.6 2 1.6 4.8 0 6.8" fill="none" stroke="var(--card-black)" stroke-width=".8"/></svg>www.corvanefx.co.nz</li>
        <li><svg viewBox="0 0 12 12" aria-hidden="true"><rect width="12" height="12" rx="1.5" fill="var(--text-light)"/><rect x="2.4" y="3.4" width="7.2" height="5.2" fill="none" stroke="var(--card-black)" stroke-width="1"/><path d="M2.4 3.4L6 6.4l3.6-3" fill="none" stroke="var(--card-black)" stroke-width="1"/></svg>desk@corvanefx.co.nz</li>
      </ul>
    </div>

    <address class="address">1148 Maple Ridge Rd<br>Linford Ohio 43990</address>
  </section>

  <section class="card card--back" aria-label="Business card back">
    <div class="brand"><span class="brand__mark"></span>Corvane Capital</div>
  </section>

</main>
</body>
</html>
```